Private Investigator needs business card with an intelligent logo

Private Investigator needs uncluttered, intelligently designed business card with simple logo. Prefer one or two colour print only. Must convey serious approach with only basic information: Business Name, "Clearmarsh Investigations"
Phone: 03 5550 1946 Email: info@clearmarsh.com.au Web: www.clearmarsh.com.au
Agents Name: Derek Hollins Title: Investigator Mobile: 0491 570 156

Thank you all very much for your designs.  There was some really excellent ideas and the choice was very hard.  I sought opinions from a number of people about which was the best one and there were a number of different choices but eventually the majority went with one design from Kavlorix.  Thank you especially to those designers that made some changes when I suggested them.

Thanks again for all your efforts and good luck with your design careers.  I will certainly use Graftnest again with the great quality of designers that made submissions.

Regards  Derek Hollins

```html
<!DOCTYPE html>
<html lang="en">
<head>
<meta charset="utf-8">
<title>Clearmarsh Investigations – Business Card</title>
<link rel="stylesheet" href="https://fonts.googleapis.com/css2?family=Open+Sans:wght@300;400&display=swap">
<style>
  :root {
    --backdrop: #c9c9c9;
    --card-white: #ffffff;
    --band-black: #262626;
    --logo-grey: #333333;
    --text-white: #ffffff;
  }
  html, body {
    margin: 0;
    width: 1200px;
    height: 985px;
    overflow: hidden;
    background: var(--backdrop);
    font-family: "Open Sans", sans-serif;
  }
  .business-card {
    position: absolute;
    left: 150px;
    top: 235px;
    width: 900px;
    height: 514px;
    background: var(--card-white);
    border-radius: 18px;
    overflow: hidden;
    box-shadow: 0 10px 30px rgba(0,0,0,0.25);
  }
  .card-band {
    position: absolute;
    inset: 0;
  }
  .band-shape { fill: var(--band-black); }
  .divider-rule { stroke: var(--text-white); stroke-width: 2; }
  .name-marker { fill: var(--text-white); }
  .brand {
    position: absolute;
    left: 40px;
    top: 58px;
    display: flex;
    align-items: flex-start;
    gap: 12px;
    color: var(--logo-grey);
  }
  .brand-square {
    width: 18px;
    height: 44px;
    background: var(--band-black);
    margin-top: 4px;
  }
  .brand-name {
    margin: 0;
    font-weight: 400;
    font-size: 34px;
    line-height: 1.05;
  }
  .brand-name span {
    display: block;
    font-size: 28px;
    letter-spacing: 1px;
  }
  .agent {
    position: absolute;
    right: 110px;
    top: 270px;
    text-align: right;
    color: var(--text-white);
  }
  .agent-name {
    margin: 0;
    font-weight: 400;
    font-size: 40px;
    line-height: 1.1;
  }
  .agent-title {
    margin: 0;
    font-size: 24px;
    line-height: 1.1;
    letter-spacing: 1px;
  }
  .contact-list {
    position: absolute;
    left: 60px;
    top: 368px;
    margin: 0;
    padding: 0;
    list-style: none;
    color: var(--text-white);
    font-weight: 300;
    font-size: 22px;
    line-height: 28px;
    letter-spacing: 2px;
  }
</style>
</head>
<body>
  <div class="business-card">
    <svg class="card-band" width="900" height="514" viewBox="0 0 900 514">
      <polygon class="band-shape" points="0,230 900,230 900,340 720,514 0,514"/>
      <line class="divider-rule" x1="330" y1="350" x2="800" y2="350"/>
      <rect class="name-marker" x="798" y="300" width="24" height="42"/>
    </svg>

    <div class="brand">
      <div class="brand-square"></div>
      <h1 class="brand-name">Clearmarsh<span>Investigations</span></h1>
    </div>

    <div class="agent">
      <p class="agent-name">Derek Hollins</p>
      <p class="agent-title">Investigator</p>
    </div>

    <ul class="contact-list">
      <li>Mobile: 0491 570 156</li>
      <li>Phone: 03 5550 1946</li>
      <li>Email: info@clearmarsh.com.au</li>
      <li>Web: www.clearmarsh.com.au</li>
    </ul>
  </div>
</body>
</html>
```